New Managed IT company needs a business card

We are an IT management and support company that needs a business card design. I have a logo that I'll provide. Blues and blacks match the logo, but i'm open to anything. I want the card to help people take us seriously, but still have some energy and fun in it. The card should communicate stability and a solid company.

Target Market(s)

Target market includes Owners and Presidents at small businesses of 20 - 100 employees in the Pittsburgh PA area.

Industry/Entity Type

Information Technology

Contact Information for Business Card

i am open to other designs, but i imagine having only the logo on one side and then the logo plus all contact details on the other side.

Requirements
Must have
• Our logo
• Company name is optional if the logo makes it obvious
• A name - Lew Tasker
• A title - President
• A phone number - 724-XXX-XXXX
• A mobile phone number - 724-516-0471
• An email address - ltasker@brightlanetech.com
• a website - brightlanetech.com or www.brightlanetech.com
Nice to have
• some people tell me the logo feels like a superhero theme, some fun with that idea might be good. I'm open to ideas.
Should not have
• stock photos of people or computers - especially old looking stuff.

```html
<!DOCTYPE html>
<html lang="en">
<head>
<meta charset="utf-8">
<title>Brightlane Tech – Business Card</title>
<link href="https://fonts.googleapis.com/css2?family=Roboto:wght@400;500;700&display=swap" rel="stylesheet">
<style>
  :root {
    --bg: #1b1b1c;
    --card: #ffffff;
    --ink: #1d1d1f;
    --ink-soft: #3a3a3c;
    --brand-blue: #1b9be0;
    --brand-blue-light: #6cc8f0;
    --rule-blue: #2fa6e6;
  }
  * { box-sizing: border-box; margin: 0; padding: 0; }
  html, body { width: 1200px; height: 952px; overflow: hidden; }
  body {
    background: var(--bg);
    font-family: "Roboto", Arial, sans-serif;
    color: var(--ink);
    position: relative;
  }
  .card {
    position: absolute;
    width: 580px;
    height: 330px;
    background: var(--card);
    border-radius: 22px;
    overflow: hidden;
  }
  .card--back { left: 570px; top: 110px; }
  .card--front { left: 60px; top: 500px; }

  .brand { display: flex; align-items: center; gap: 12px; }
  .brand__dot {
    width: 44px; height: 44px; border-radius: 50%;
    background: var(--brand-blue);
    flex: none;
  }
  .brand__name {
    font-weight: 700;
    font-size: 30px;
    letter-spacing: 3px;
    text-transform: uppercase;
    color: var(--ink-soft);
    line-height: 1;
  }

  .card--back .brand {
    position: absolute; left: 0; right: 0; top: 120px;
    justify-content: center;
  }
  .card--back .site {
    position: absolute; left: 0; right: 0; bottom: 48px;
    text-align: center;
    color: var(--brand-blue);
    font-size: 18px;
    letter-spacing: 0.5px;
  }

  .card--front .brand { position: absolute; left: 40px; top: 36px; }
  .person { position: absolute; left: 40px; top: 104px; }
  .person__name { color: var(--brand-blue); font-size: 26px; font-weight: 500; }
  .person__title { font-size: 17px; color: var(--ink); margin-top: 2px; }
  .divider {
    position: absolute; left: 126px; top: 163px;
    width: 380px; height: 1.5px;
    background: linear-gradient(90deg, var(--rule-blue), rgba(47,166,230,0.15));
  }
  .contacts {
    position: absolute; right: 30px; top: 190px;
    list-style: none;
    display: flex; flex-direction: column; gap: 6px;
    align-items: flex-end;
  }
  .contacts li { display: flex; align-items: center; gap: 10px; font-size: 19px; }
  .contacts li.email { color: var(--ink-soft); }
  .icon {
    width: 24px; height: 24px; border-radius: 50%;
    background: var(--brand-blue);
    display: flex; align-items: center; justify-content: center;
    flex: none;
  }
  .icon svg { width: 14px; height: 14px; fill: none; stroke: #fff; stroke-width: 1.8; stroke-linecap: round; stroke-linejoin: round; }
  .accent-band {
    position: absolute; right: 0; bottom: 0; width: 580px; height: 330px;
  }
</style>
</head>
<body>

  <section class="card card--back" aria-label="Card back">
    <div class="brand">
      <span class="brand__dot"></span>
      <span class="brand__name">Brightlane Tech</span>
    </div>
    <p class="site">www.brightlanetech.com</p>
  </section>

  <section class="card card--front" aria-label="Card front">
    <svg class="accent-band" viewBox="0 0 580 330" aria-hidden="true">
      <defs>
        <linearGradient id="bandFill" x1="0" y1="0" x2="1" y2="1">
          <stop offset="0" stop-color="#7fd0f3"/>
          <stop offset="1" stop-color="#1696de"/>
        </linearGradient>
      </defs>
      <path d="M300 330 C330 300 360 296 400 300 L580 304 L580 330 Z" fill="url(#bandFill)"/>
    </svg>

    <div class="brand">
      <span class="brand__dot"></span>
      <span class="brand__name">Brightlane Tech</span>
    </div>

    <div class="person">
      <p class="person__name">Lew Tasker</p>
      <p class="person__title">President</p>
    </div>
    <div class="divider"></div>

    <ul class="contacts">
      <li>724-XXX-XXXX
        <span class="icon"><svg viewBox="0 0 16 16"><path d="M3 3c1-1 2-1 3 0l1 2-1.5 1.5c.8 1.7 2.3 3.2 4 4L11 9l2 1c1 1 1 2 0 3-2 1.5-5 .5-7.5-2S1.5 5 3 3z"/></svg></span>
      </li>
      <li>724-516-0471
        <span class="icon"><svg viewBox="0 0 16 16"><rect x="4.5" y="1.5" width="7" height="13" rx="1.5"/><path d="M7 12.5h2"/></svg></span>
      </li>
      <li class="email">ltasker@brightlanetech.com
        <span class="icon"><svg viewBox="0 0 16 16"><rect x="2" y="4" width="12" height="8.5" rx="1"/><path d="M2 4.5l6 4.5 6-4.5"/></svg></span>
      </li>
      <li>www.brightlanetech.com
        <span class="icon"><svg viewBox="0 0 16 16"><circle cx="8" cy="8" r="6"/><path d="M2 8h12M8 2c2 2 2 10 0 12M8 2c-2 2-2 10 0 12"/></svg></span>
      </li>
    </ul>
  </section>

</body>
</html>
```